Electrician Business Card/ company logo/small business

New Business Cards and logo needed that will catch peoples eye and say we went that extra step. Attached is a design possibly to be incorporated, if u have your own great, lets see it!... This will be a small local business. thank you for all you do!
Quorvane Electric
Dov Merrick Owner
Journeyman Electrician
phone 1.482.639.2075
email: QRTQuorvaneElectric@zentromail.com
call for free estimate!
Updates

Accepted and approved for cards

Target Market(s)

support small local business

Industry/Entity Type

Electrical,

Contact Information for Business Card

name, title,company/ logo, phone, email, free estimate

Font styles to use
Other font styles liked:
• easy to read

Colors

Designer to choose colors to be used in the design.

Requirements
Must have
• eye catching everything! logo and quorvane electric listed on business card/logo, incorp logo in the background of card
Nice to have
• lightening bolts in eyes or around the triangle? vertical, modern, any design that would be unique and stand out
Should not have
• pinks, reds, yellows,brown

```html
<!DOCTYPE html>
<html lang="en">
<head>
<meta charset="utf-8">
<title>Quorvane Electric – Business Card</title>
<link rel="stylesheet" href="https://fonts.googleapis.com/css2?family=Michroma&family=Montserrat:wght@500;600;700&display=swap">
<style>
  :root {
    --backdrop: #d4d5d8;
    --card: #262626;
    --facet-light: #2f3030;
    --facet-mid: #2b2b2b;
    --green: #8cc11f;
    --green-line: #5fb31c;
    --white: #ffffff;
    --ink: #2a2a2a;
  }
  * { margin: 0; padding: 0; box-sizing: border-box; }
  html, body { width: 1200px; height: 1200px; overflow: hidden; }
  body {
    position: relative;
    background: var(--backdrop);
    font-family: "Montserrat", sans-serif;
  }
  .card {
    position: absolute;
    left: 74px; top: 180px;
    width: 450px; height: 806px;
    background: var(--card);
    overflow: hidden;
  }
  .card-facets { position: absolute; inset: 0; }
  .brand {
    position: absolute;
    right: 44px; top: 112px;
    display: flex; align-items: center; gap: 16px;
  }
  .brand-mark {
    width: 30px; height: 30px;
    background: var(--green);
    flex: none;
  }
  .brand-name {
    font-family: "Michroma", sans-serif;
    font-size: 25px;
    color: var(--green);
    line-height: 1.45;
    text-align: right;
    white-space: nowrap;
  }
  .holder-name {
    position: absolute;
    left: 42px; top: 388px;
    font-family: "Michroma", sans-serif;
    font-weight: 400;
    font-size: 30px;
    color: var(--green);
    letter-spacing: 3px;
    white-space: nowrap;
  }
  .holder-role {
    position: absolute;
    left: 42px; top: 435px;
    font-weight: 600;
    font-size: 23px;
    color: var(--white);
    letter-spacing: 1.5px;
  }
  .divider {
    position: absolute;
    left: 42px; right: 0; top: 481px;
    height: 3px;
    background: var(--green-line);
  }
  .holder-trade {
    position: absolute;
    left: 42px; top: 497px;
    font-weight: 500;
    font-size: 24px;
    color: var(--white);
    white-space: nowrap;
  }
  .contact-row {
    position: absolute;
    left: 42px;
    display: flex; align-items: center; gap: 12px;
    color: var(--white);
    font-weight: 700;
    white-space: nowrap;
  }
  .contact-row.phone { top: 621px; font-size: 30px; }
  .contact-row.email { top: 681px; font-size: 16px; }
  .contact-icon {
    width: 40px; height: 38px;
    background: linear-gradient(135deg, #a6d12a, #6fae1c);
    display: flex; align-items: center; justify-content: center;
    flex: none;
  }
  .lockup {
    position: absolute;
    right: 74px; top: 556px;
    display: flex; align-items: center; gap: 22px;
  }
  .lockup .brand-mark { width: 44px; height: 44px; background: var(--ink); }
  .lockup .brand-name { color: var(--ink); font-size: 30px; }
</style>
</head>
<body>
  <section class="card">
    <svg class="card-facets" width="450" height="806" viewBox="0 0 450 806">
      <polygon points="0,0 450,0 450,130 220,40 0,110" fill="var(--facet-mid)"/>
      <polygon points="0,110 220,40 450,130 450,210 150,290 0,230" fill="var(--facet-light)"/>
      <polygon points="0,230 150,290 0,300" fill="#2c2d2d"/>
      <polygon points="150,290 450,210 450,380 250,290" fill="#2a2a2a"/>
    </svg>

    <div class="brand">
      <span class="brand-mark"></span>
      <span class="brand-name">QUORVANE<br>Electric</span>
    </div>

    <h1 class="holder-name">DOV MERRICK</h1>
    <p class="holder-role">OWNER</p>
    <div class="divider"></div>
    <p class="holder-trade">JOURNEYMAN ELECTRICIAN</p>

    <div class="contact-row phone">
      <span class="contact-icon">
        <svg width="22" height="22" viewBox="0 0 24 24" fill="none" stroke="#2a4a0a" stroke-width="1.4">
          <path d="M5 3h4l2 5-2.5 1.5a11 11 0 0 0 6 6L16 13l5 2v4a2 2 0 0 1-2 2A16 16 0 0 1 3 5a2 2 0 0 1 2-2z"/>
        </svg>
      </span>
      <span>1.482.639.2075</span>
    </div>
    <div class="contact-row email">
      <span class="contact-icon">
        <svg width="24" height="18" viewBox="0 0 24 18" fill="none" stroke="#2a4a0a" stroke-width="1.4">
          <rect x="1" y="1" width="22" height="16"/>
          <path d="M1 1l11 9 11-9M1 17l8-7M23 17l-8-7"/>
        </svg>
      </span>
      <span>QRTQuorvaneElectric@zentromail.com</span>
    </div>
  </section>

  <div class="lockup">
    <span class="brand-mark"></span>
    <span class="brand-name">QUORVANE<br>Electric</span>
  </div>
</body>
</html>
```